Road Sign at our office 84 in X 48 in - Small Billboard

Kestrel Electrical
Electrical & Lighting Services

- we need a sign design for our small business/company based in Calhoun, GA called Kestrel Electrical - "our mission is to provide Northwest Georgia with dependable, high-quality electrical services that prioritize safety, integrity, and long-term reliability. As a woman-owned business with over 25 years of experience, we are committed to delivering exceptional workmanship and personalized service for every commercial, residential, and industrial project we undertake. We stand behind our work with a lifetime warranty—because your trust is our most powerful connection."

display logo, phone number, and open to other ideas without being cluttered, maybe instead of full website address, just use @ksrelectrical and it will send them to all of our website and socials...

it needs to be easy to read as they drive down the road
this is a place where people may be traveling at high speeds, make sure it's easy to see and understand at a glance.
It will be hanging 20-24ft from the ground. Like a small billboard.

https://ksrelectricworks.com/

Industry/Entity Type

Electrical Contractor

Requirements
Nice to have
• match the look and feel of website and socials

```html
<!DOCTYPE html>
<html lang="en">
<head>
<meta charset="utf-8">
<title>Kestrel Electrical – Road Sign</title>
<link rel="stylesheet" href="https://fonts.googleapis.com/css2?family=Montserrat:wght@500;600&family=Oswald:wght@500;600&display=swap">
<style>
  :root {
    --backdrop: #e9eaec;
    --sign-black: #000000;
    --brand-white: #ffffff;
    --brand-orange: #f39200;
    --brand-red-orange: #e84e1b;
    --ink: #111111;
    --rule-light: #e6e6e6;
  }
  html, body {
    margin: 0;
    padding: 0;
    width: 1200px;
    height: 1157px;
    overflow: hidden;
    background: var(--backdrop);
  }
  .sign {
    position: absolute;
    left: 0;
    top: 321px;
    width: 1200px;
    height: 514px;
    background: var(--sign-black);
    overflow: hidden;
  }
  .brand {
    position: absolute;
    left: 0;
    right: 0;
    top: 52px;
    display: flex;
    justify-content: center;
    align-items: center;
    gap: 22px;
  }
  .brand-dot {
    width: 74px;
    height: 74px;
    border-radius: 50%;
    background: var(--brand-orange);
  }
  .brand-name {
    font-family: "Montserrat", sans-serif;
    font-weight: 600;
    color: var(--brand-white);
    line-height: 1;
  }
  .brand-name .word {
    display: block;
    font-size: 66px;
    letter-spacing: -0.5px;
  }
  .brand-name .sub {
    display: block;
    font-size: 27px;
    letter-spacing: 17px;
    margin-top: 8px;
  }
  .tagline {
    position: absolute;
    left: 0;
    right: 0;
    top: 238px;
    margin: 0;
    text-align: center;
    font-family: "Oswald", sans-serif;
    font-weight: 500;
    font-size: 74px;
    line-height: 1;
    letter-spacing: 4px;
    color: var(--brand-orange);
    text-transform: uppercase;
  }
  .divider {
    position: absolute;
    left: 257px;
    width: 686px;
    top: 339px;
    height: 5px;
    border-radius: 3px;
    background: linear-gradient(90deg, rgba(230,230,230,0) 0%, #6a6a6a 25%, var(--rule-light) 50%, #6a6a6a 75%, rgba(230,230,230,0) 100%);
  }
  .contact-band {
    position: absolute;
    left: 0;
    bottom: 0;
    width: 1200px;
    height: 114px;
    display: block;
  }
  .phone {
    position: absolute;
    left: 28px;
    bottom: 8px;
    font-family: "Oswald", sans-serif;
    font-weight: 600;
    font-size: 100px;
    line-height: 1;
    letter-spacing: 3px;
    color: var(--brand-white);
  }
  .handle {
    position: absolute;
    right: 38px;
    bottom: 28px;
    font-family: "Montserrat", sans-serif;
    font-weight: 500;
    font-size: 58px;
    line-height: 1;
    color: var(--ink);
  }
</style>
</head>
<body>
  <main class="sign">
    <div class="brand">
      <span class="brand-dot"></span>
      <div class="brand-name">
        <span class="word">Kestrel</span>
        <span class="sub">ELECTRICAL</span>
      </div>
    </div>

    <h1 class="tagline">Electrical &amp; Lighting Services</h1>
    <div class="divider"></div>

    <svg class="contact-band" viewBox="0 0 1200 114" preserveAspectRatio="none" aria-hidden="true">
      <rect x="0" y="0" width="1200" height="114" fill="var(--brand-orange)"/>
      <polygon points="0,0 640,0 698,114 0,114" fill="var(--brand-red-orange)"/>
    </svg>
    <div class="phone">706-555-0148</div>
    <div class="handle">@ksrelectrical</div>
  </main>
</body>
</html>
```